Asia based real estate financing firm needs and AWESOME design for a biz card -Harbor Lending Circle

Looking for a stylish, & corporate-looking business card for a real estate financing brokerage firm in Asia, offering global mortgage loans. I uploaded our current logos. We would like to add a splash of color (perhaps the house icon) or any other suggestions are open. For the winning designer, we have a lot of work! Thanks and best of luck!

Target Market(s)

Real estate investors globally. We want to look more like a BANK and NOT a real estate company. Please don't play up on a "house" design.

Industry/Entity Type

Banking

Contact Information for Business Card

Harbor Lending Circle
Peter Wilks
Co-Founder | Partner

14 Cassia Lane, Suite 310
Singapore 047219
www.hlc-example.asia
peterwilks@hlc-example.asia
+65 555-0142
Chat ID: peterwilks

Colors

Designer to choose colors to be used in the design.

Requirements
Must have
• Must have the standard business requirements for a card; name, address, email, etc
• Can be horizontal or vertical.
Nice to have
• It would be great to see some sort of variation to the logo with a pop of color. Red is good as we're in Asia, however, other options work as well.
• Our tag line is - Lending Beyond Shores. It doesn't have to be on the card but might be nice.
• I'd like to start seeing our tagline within the cards as well. - Lending Beyond Shores.
• Also, please add our location. The location for this card is Singapore so perhaps it can be highlighted or emphasised in some way.
• Singapore | Hong Kong | Shanghai | Manila
• As we will soon open an office in Shanghai, having an option for both languages would be great.
Should not have
• I'm exceited and open to your creativity ... knock it out of the park!

```html
<!DOCTYPE html>
<html lang="en">
<head>
<meta charset="utf-8">
<title>Harbor Lending Circle – Business Card</title>
<link href="https://fonts.googleapis.com/css2?family=Montserrat:wght@300;400;600;700&display=swap" rel="stylesheet">
<style>
  :root {
    --backdrop: #24272c;
    --card: #111b2b;
    --card-edge: #0b1320;
    --accent: #e3121c;
    --ink: #f4f5f7;
  }
  * { box-sizing: border-box; margin: 0; padding: 0; }
  html, body { width: 1200px; height: 900px; overflow: hidden; }
  body {
    background: var(--backdrop);
    font-family: "Montserrat", sans-serif;
    display: flex;
    flex-direction: column;
    align-items: center;
    justify-content: center;
    gap: 40px;
  }
  .card {
    width: 700px;
    height: 400px;
    background: var(--card);
    border-radius: 28px;
    box-shadow: 0 6px 0 var(--card-edge), 0 18px 40px rgba(0,0,0,.45);
    position: relative;
  }
  /* Front */
  .card--front {
    display: flex;
    flex-direction: column;
    align-items: center;
    justify-content: center;
    gap: 34px;
  }
  .brand-name {
    color: var(--accent);
    font-weight: 600;
    font-size: 38px;
    letter-spacing: 1px;
  }
  .tagline {
    color: var(--accent);
    font-weight: 400;
    font-size: 15px;
    letter-spacing: 11px;
    text-transform: uppercase;
  }
  /* Back */
  .card--back {
    display: grid;
    grid-template-columns: 290px 1fr;
    align-items: center;
    padding: 0 40px 0 44px;
  }
  .card--back .brand-name {
    font-size: 24px;
    line-height: 1.25;
  }
  .contact-name {
    color: var(--ink);
    font-weight: 700;
    font-size: 24px;
  }
  .contact-role {
    color: var(--accent);
    font-size: 13px;
    margin: 4px 0 20px;
  }
  .contact-list { list-style: none; }
  .contact-item {
    display: flex;
    align-items: flex-start;
    gap: 12px;
    color: var(--ink);
    font-size: 13px;
    letter-spacing: 1.5px;
    line-height: 1.45;
    margin-bottom: 6px;
  }
  .contact-item svg { flex: none; width: 14px; height: 14px; margin-top: 2px; fill: var(--accent); }
  .label { color: var(--accent); }
</style>
</head>
<body>
  <section class="card card--front">
    <div class="brand-name">Harbor Lending Circle</div>
    <div class="tagline">Lending Beyond Shores</div>
  </section>

  <section class="card card--back">
    <div class="brand-name">Harbor<br>Lending Circle</div>
    <div class="contact">
      <div class="contact-name">Peter Wilks</div>
      <div class="contact-role">Co-Founder | Partner</div>
      <ul class="contact-list">
        <li class="contact-item">
          <svg viewBox="0 0 24 24"><path d="M12 1a8 8 0 0 0-8 8c0 6 8 14 8 14s8-8 8-14a8 8 0 0 0-8-8zm0 11a3 3 0 1 1 0-6 3 3 0 0 1 0 6z"/></svg>
          <span>14 Cassia Lane, Suite 310<br>Singapore 047219</span>
        </li>
        <li class="contact-item">
          <svg viewBox="0 0 24 24"><path d="M7 1h10a2 2 0 0 1 2 2v18a2 2 0 0 1-2 2H7a2 2 0 0 1-2-2V3a2 2 0 0 1 2-2zm0 3v14h10V4z"/></svg>
          <span>+65 555-0142</span>
        </li>
        <li class="contact-item">
          <svg viewBox="0 0 24 24"><path d="M2 5h20v14H2zm2 2v.5l8 5 8-5V7z"/></svg>
          <span>peterwilks@hlc-example.asia</span>
        </li>
        <li class="contact-item">
          <svg viewBox="0 0 24 24"><path d="M12 2a10 10 0 1 0 0 20 10 10 0 0 0 0-20zm6.9 9h-3a15 15 0 0 0-1.4-6 8 8 0 0 1 4.4 6zM12 4c1 1.4 1.8 4 1.9 7h-3.8C10.2 8 11 5.4 12 4zM9.5 5a15 15 0 0 0-1.4 6h-3a8 8 0 0 1 4.4-6zm-4.4 8h3a15 15 0 0 0 1.4 6 8 8 0 0 1-4.4-6zm6.9 7c-1-1.4-1.8-4-1.9-7h3.8c-.1 3-.9 5.6-1.9 7zm2.5-1a15 15 0 0 0 1.4-6h3a8 8 0 0 1-4.4 6z"/></svg>
          <span>www.hlc-example.asia</span>
        </li>
        <li class="contact-item">
          <span><span class="label">Chat ID:</span> peterwilks</span>
        </li>
      </ul>
    </div>
  </section>
</body>
</html>
```